Sign Shop website

We need a web design for a sign company called Quillby Signs that builds signs for shops such as A Frames, Banners, Tennet Boards, Shop front windows etc...

The existing site is avaliable at www.quillbysigns.com.au

We will need to have a fresh makeover. The new site must have the following:

Photo Galleries (broken down into sections)
Store Locations (currently there are 4 stores)
Online quote form
List of services
About Us Page

We just need to front page designed in photoshop (the inner page is not necessary) We have a team that can code the site up.

The website should have the exact logo. Any person who alters the logo, design will be elimated.

No Twitter, RSS, LinkedIn icons

The main colours are yellow, black, blue, red

Target Market(s)

Any business

Industry/Entity Type

It Company

Requirements
Must have
• jQuery slider banner
Should not have
• Alter the logo in any way

```html
<!DOCTYPE html>
<html lang="en">
<head>
<meta charset="utf-8">
<title>Quillby Signs</title>
<link rel="stylesheet" href="https://fonts.googleapis.com/css2?family=Arimo:wght@400;700&family=Gelasio:wght@400;700&display=swap">
<style>
:root{
  --yellow:#ebb02f;
  --red:#e1412a;
  --red-dark:#c7331f;
  --blue:#1a4fc0;
  --blue-dark:#133a96;
  --ink:#222;
  --nav:#1d1d21;
  --hero:#e0e0e0;
  --grey-panel:#4a4a4a;
  --dark-panel:#1b1a20;
  --rule:#cfcfcf;
  --footbar:#dcdcdc;
  --white:#fff;
}
*{box-sizing:border-box;margin:0;padding:0}
html,body{width:1200px;height:1142px;overflow:hidden;background:var(--white)}
body{position:relative;font-family:"Arimo",Arial,sans-serif;color:var(--ink)}
.abs{position:absolute}
.serif{font-family:"Gelasio",Georgia,serif}

.top-email{left:840px;top:13px;width:191px;text-align:right;font-size:11.5px}
.top-email b{color:var(--red)}
.brand-band{left:0;top:34px}
.brand{left:176px;top:56px;font-family:"Gelasio",Georgia,serif;font-weight:700;font-size:44px;color:#2b1f4f;display:flex;align-items:center;gap:12px}
.brand i{display:block;width:22px;height:22px;background:var(--red)}
.main-nav{left:622px;top:46px;width:578px;height:32px;background:var(--nav);display:flex;padding-left:21px}
.main-nav a{color:#fff;text-decoration:none;font-size:12.5px;line-height:32px;padding:0 14px;border-right:1px dotted #666}
.main-nav a.active{background:var(--red);padding:0 17px}

.hero{left:0;top:148px;width:1200px;height:334px;background:var(--hero);overflow:hidden}
.hero-title{left:169px;top:199px;font-size:31px;color:var(--blue)}
.hero-text{left:169px;top:247px;width:335px;font-size:13.3px;line-height:16px;color:#222}
.btn{display:block;color:#fff;font-family:"Gelasio",Georgia,serif;font-weight:700;text-decoration:none;background:var(--red);clip-path:polygon(0 0,100% 0,88% 100%,0 100%);}
.btn-shadow{background:#9a9a9a;clip-path:polygon(0 0,100% 0,88% 100%,0 100%)}
.enquire{left:169px;top:343px;width:200px;height:38px}
.enquire .btn{width:188px;height:38px;font-weight:400;font-size:17px;padding:9px 0 0 16px}
.dots{left:169px;top:424px;display:flex;gap:9px}
.dots span{width:16px;height:16px;border-radius:50%;background:var(--nav)}
.dots span:first-child{background:var(--yellow)}
.monitor{left:547px;top:103px;width:483px;height:292px;background:#111;border-radius:12px;border:2px solid #333}
.screen-photo{left:565px;top:120px;width:449px;height:257px;background:linear-gradient(180deg,#eceef2 0%,#d6d8dc 30%,#5b4a3c 55%,#3a3128 100%)}
.stand{left:707px;top:395px}

.box-title{height:37px;background:linear-gradient(180deg,var(--blue),var(--blue-dark));color:#fff;font-family:"Gelasio",Georgia,serif;font-size:21px;line-height:37px;padding-left:10px;box-shadow:0 0 0 3px #e9e9e9}
.col-divider{width:1px;height:251px;background:var(--rule);top:508px}
.services{left:169px;top:508px;width:206px}
.service-list{list-style:none;margin-top:8px}
.service-list li{height:29.7px;line-height:28px;font-size:12.5px;padding-left:20px;border-bottom:1px dotted #999;position:relative}
.service-list li::before{content:"";position:absolute;left:6px;top:10px;border-left:6px solid var(--red);border-top:4px solid transparent;border-bottom:4px solid transparent}
.service-list li.current{background:#dedede}
.welcome{left:430px;top:508px;width:335px}
.welcome-text{left:434px;top:559px;width:197px;font-size:11.2px;line-height:14.2px;text-align:justify;color:#333}
.badge{left:657px;top:560px;width:105px;height:123px;background:#e8e8e8;border:1px solid #ccc}
.about-btn{left:435px;top:732px;width:118px;height:25px}
.about-btn .btn{width:112px;height:25px;font-size:14px;padding:4px 0 0 15px}
.stores{left:819px;top:508px;width:211px}
.store{left:827px;width:203px;height:59px;display:flex;align-items:center}
.store-num{width:34px;height:34px;border-radius:50%;background:var(--red);color:#fff;font-weight:700;font-size:18px;text-align:center;line-height:34px;margin-right:11px}
.store p{font-size:12.5px;line-height:15px}
.store-rule{left:827px;width:203px;border-top:1px dotted #999}

.footer-panels{left:0;top:804px}
.panel-title{font-family:"Gelasio",Georgia,serif;font-size:21px;color:#fff}
.panel-rule{height:1px;background:#777}
.form-label{font-size:11.3px;color:#fff}
.field{height:16px;background:#fff;border:1px solid #888}
.select::after{content:"";position:absolute;right:1px;top:1px;width:12px;height:12px;background:#ddd;border:1px solid #999}
.submit{left:233px;top:1059px;width:105px;height:25px}
.submit .btn,.viewall .btn{background:var(--yellow);color:#222;width:100%;height:25px;font-size:14px;padding:4px 0 0 14px;box-shadow:inset 4px 0 0 #a07a1c}
.viewall{left:731px;top:1059px;width:100px;height:25px}
.thumb{width:142px;height:85px;border:3px solid #fff}
.bottom-bar{left:0;top:1103px;width:1200px;height:39px;background:var(--footbar)}
.foot-links{left:169px;top:1116px;font-size:11.5px;display:flex;gap:14px}
.foot-links a{color:#222;text-decoration:none}
.foot-links a.active{color:var(--red);text-decoration:underline}
.copyright{left:700px;top:1116px;width:331px;text-align:right;font-size:11.5px}
</style>
</head>
<body>

<header>
  <div class="abs top-email"><b>Email :</b> info@quillbysigns.com.au</div>
  <svg class="abs brand-band" width="640" height="52" viewBox="0 0 640 52"><polygon points="0,0 622,0 588,52 0,52" fill="var(--yellow)"/></svg>
  <div class="abs brand"><i></i>Quillby Signs</div>
  <nav class="abs main-nav">
    <a class="active" href="#">Home</a><a href="#">About Us</a><a href="#">Services</a><a href="#">Portfolio</a><a href="#">Contact Us</a>
  </nav>
</header>

<section class="abs hero">
  <svg width="1200" height="334" viewBox="0 0 1200 334"><polygon points="864,0 1200,0 1200,334 531,334" fill="var(--yellow)"/></svg>
</section>
<h1 class="abs hero-title serif" style="font-weight:400">Sign Solutions</h1>
<p class="abs hero-text">Quillby Signs will exceed customer expectations by offering a personalised approach to clients, embracing and executing individual needs through a comprehensive range of services.</p>
<div class="abs enquire"><div class="abs btn-shadow" style="left:10px;top:0;width:190px;height:38px"></div><a class="abs btn" href="#">Enquare Now</a></div>
<div class="abs dots"><span></span><span></span><span></span><span></span></div>
<div class="abs monitor"></div>
<div class="abs screen-photo" role="img" aria-label="Photo of a finished shopfront sign and window lettering"></div>
<svg class="abs stand" width="160" height="62" viewBox="0 0 160 62"><defs><linearGradient id="steel" x1="0" x2="1"><stop offset="0" stop-color="#9a9a9a"/><stop offset=".5" stop-color="#f2f2f2"/><stop offset="1" stop-color="#8a8a8a"/></linearGradient></defs><path d="M52 0 H108 L116 46 H44 Z" fill="url(#steel)"/><ellipse cx="80" cy="52" rx="72" ry="9" fill="url(#steel)"/></svg>

<main>
  <section class="abs services">
    <h2 class="box-title" style="font-weight:400">Our Services</h2>
    <ul class="service-list">
      <li class="current">Quality Stickers &amp; Decals</li>
      <li>All Sign Types</li>
      <li>Vehicle Signage</li>
      <li>Magnets</li>
      <li>Construction and safety Signs</li>
      <li>Window Signage</li>
      <li>Laminating</li>
    </ul>
  </section>
  <div class="abs col-divider" style="left:403px"></div>
  <section class="abs welcome"><h2 class="box-title" style="font-weight:400">Welcome to Quillby Signs</h2></section>
  <p class="abs welcome-text">Quillby Signs is a West Australian owned and managed company. We manufacture signage for any application; vinyl lettering, pull up banners, vehicle signage.In fact anything that requires our customers seeing the full picture when it comes to advertising their business. So if you're serious about the best, put us to the test!</p>
  <div class="abs badge" role="img" aria-label="Locally owned badge"></div>
  <div class="abs about-btn"><div class="abs btn-shadow" style="left:8px;top:0;width:110px;height:25px"></div><a class="abs btn" href="#">About Us</a></div>
  <div class="abs col-divider" style="left:792px"></div>
  <section class="abs stores"><h2 class="box-title" style="font-weight:400">Store Locations</h2></section>
  <div class="abs store" style="top:554px"><div class="store-num">1</div><p>Willetton<br>(08) 5550 1842</p></div>
  <div class="abs store-rule" style="top:614px"></div>
  <div class="abs store" style="top:613px"><div class="store-num">2</div><p>Joondalup<br>(08) 5550 2317</p></div>
  <div class="abs store-rule" style="top:673px"></div>
  <div class="abs store" style="top:671px"><div class="store-num">3</div><p>South Lakes<br>(08) 5550 2317</p></div>
</main>

<footer>
  <svg class="abs footer-panels" width="1200" height="299" viewBox="0 0 1200 299"><rect width="1200" height="299" fill="var(--dark-panel)"/><polygon points="0,0 731,0 552,299 0,299" fill="var(--grey-panel)"/></svg>

  <h3 class="abs panel-title" style="left:169px;top:813px;font-weight:400">Request A Quote</h3>
  <div class="abs panel-rule" style="left:169px;top:845px;width:398px"></div>
  <span class="abs form-label" style="left:170px;top:855px">Name:</span><div class="abs field" style="left:232px;top:855px;width:112px"></div>
  <span class="abs form-label" style="left:170px;top:876px">Phone:</span><div class="abs field" style="left:232px;top:876px;width:112px"></div>
  <span class="abs form-label" style="left:170px;top:897px">Suburb:</span><div class="abs field" style="left:232px;top:897px;width:112px"></div>
  <span class="abs form-label" style="left:360px;top:855px">Company:</span><div class="abs field" style="left:453px;top:855px;width:114px"></div>
  <span class="abs form-label" style="left:360px;top:876px">Email:</span><div class="abs field" style="left:453px;top:876px;width:114px"></div>
  <span class="abs form-label" style="left:360px;top:897px">Store:</span><div class="abs field select" style="left:453px;top:897px;width:114px"></div>
  <div class="abs panel-rule" style="left:169px;top:927px;width:398px"></div>
  <span class="abs form-label" style="left:170px;top:945px">Sign Type:</span><div class="abs field" style="left:232px;top:945px;width:112px"></div>
  <span class="abs form-label" style="left:170px;top:967px">Sign Size:</span><div class="abs field" style="left:232px;top:967px;width:112px"></div>
  <span class="abs form-label" style="left:360px;top:945px">Material:</span><div class="abs field" style="left:453px;top:945px;width:114px"></div>
  <span class="abs form-label" style="left:360px;top:967px">Artwork Required:</span><div class="abs field select" style="left:453px;top:967px;width:114px"></div>
  <span class="abs form-label" style="left:170px;top:993px;line-height:14px">Others<br>Information:</span><div class="abs field" style="left:233px;top:997px;width:334px;height:43px"></div>
  <div class="abs submit"><a class="btn" href="#">Submit</a></div>

  <h3 class="abs panel-title" style="left:730px;top:813px;font-weight:400">Photo Gallery</h3>
  <div class="abs panel-rule" style="left:730px;top:845px;width:300px"></div>
  <div class="abs thumb" style="left:730px;top:856px;background:linear-gradient(160deg,#d9d9d9,#9c9c9c)" role="img" aria-label="Vehicle signage on a rear car window"></div>
  <div class="abs thumb" style="left:888px;top:856px;background:linear-gradient(135deg,#f3f3f3,#d9523f 60%,#2d5aa8)" role="img" aria-label="Collection of safety and warning signs"></div>
  <div class="abs thumb" style="left:730px;top:956px;background:linear-gradient(90deg,#f2d21b,#1e1e1e 50%,#f2d21b)" role="img" aria-label="Yellow construction caution signs"></div>
  <div class="abs thumb" style="left:888px;top:956px;background:linear-gradient(180deg,#8a3a5a,#c9a6a0 50%,#6e5a55)" role="img" aria-label="Shop front window graphics"></div>
  <div class="abs viewall"><a class="btn" href="#">View All</a></div>

  <div class="abs bottom-bar"></div>
  <nav class="abs foot-links"><a class="active" href="#">Home</a><span>|</span><a href="#">About Us</a><span>|</span><a href="#">Services</a><span>|</span><a href="#">Portfolio</a><span>|</span><a href="#">Contact Us</a></nav>
  <p class="abs copyright">Copyright© <b>Quillby Signs</b> 2013.All Right Reserved</p>
</footer>

</body>
</html>
```